Website Redesign for Asset Management

We need a full redesign on the website for Velquist Asset Management. Velquist is an asset manager that manages both long - only products and alternative investments. We would like to see a clean and innovative website that showcases the products of the firm and the management of the firm.
www.velquist.example

Output should be in PSD and designer should have groups/layers for the developer to extract the imagesĀ 

Feel free to play with the colours as we are not stuck to current colours.

Target Market(s)

The target market are affluent individuals, pensions, foundations and endowments

Industry/Entity Type

Asset Management

Requirements
Must have
• We like the websites
www.dalbrenholt.example
www.kestrafund.example
DO LIKE
http://www.norvanta.example/#Home
http://www.dalbrenholt.example/who-we-are/principals.html
http://www.qlendry.example/default.aspx
http://www.kv3.example/
http://www.morvainpell.example/Home
https://www.halvorenfund.example/index.asp
http://www.ostrela.example/Home_Page.html
http://www.rdgulvo.example/#!contact/c16fm
http://www.pikemerefund.example/
http://www.varnelo.example/
https://www.quorvelpartners.example/
http://www.dxmrf.example/
http://www.fendrickco.example/

Don't Like
http://www.tellowayasset.example
http://klavin.example/
http://rmobrand.example/
http://www.tkwilder.example/operations_team.html

Also must have a section entitles Alternative Investments

```html
<!DOCTYPE html>
<html lang="en">
<head>
<meta charset="utf-8">
<title>Velquist Asset Management</title>
<link href="https://fonts.googleapis.com/css2?family=Open+Sans:wght@400;600;700&family=Cinzel:wght@500&display=swap" rel="stylesheet">
<style>
  :root {
    --purple-deep: #2b1d44;
    --purple: #3b2a58;
    --purple-text: #3a2a64;
    --gold: #8b8452;
    --gold-light: #a29a63;
    --ink: #2f2f2f;
    --body: #777;
    --white: #fff;
    --hero-a: #6f8fb5;
    --hero-b: #2c3a52;
  }
  * { margin: 0; padding: 0; box-sizing: border-box; }
  html, body { width: 1003px; height: 1200px; overflow: hidden; background: var(--white); }
  body { position: relative; font-family: "Open Sans", sans-serif; color: var(--ink); }
  .abs { position: absolute; }

  .site-header { left: 0; top: 0; width: 1003px; height: 92px;
    background: linear-gradient(180deg, #3d2d5c 0%, var(--purple-deep) 100%); }
  .brand-plate { left: 0; top: 0; }
  .brand-name { left: 68px; top: 30px; font-family: "Cinzel", serif; font-size: 28px; font-weight: 500; color: #1c1a12; letter-spacing: 0.5px; }
  .main-nav { left: 295px; top: 50px; display: flex; gap: 25px; }
  .main-nav a { color: var(--white); text-decoration: none; font-size: 14px; font-weight: 600; }

  .hero { left: 0; top: 92px; width: 1003px; height: 385px;
    background: linear-gradient(180deg, #aebfd6 0%, var(--hero-a) 35%, var(--hero-b) 100%); }
  .hero-title { left: 0; width: 1000px; text-align: center; color: var(--white); font-weight: 700; text-transform: uppercase; text-shadow: 0 2px 6px rgba(0,0,0,.35); line-height: 1; }
  .hero-title.line-1 { top: 203px; font-size: 42px; }
  .hero-title.line-2 { top: 246px; font-size: 52px; }
  .hero-arrow { top: 250px; }
  .hero-dots { left: 476px; top: 455px; display: flex; gap: 5px; }
  .hero-dots span { width: 10px; height: 10px; border-radius: 50%; background: rgba(255,255,255,.6); }
  .hero-dots span.active { background: #333; }

  .section-title { font-weight: 400; line-height: 1; }
  .about-title { left: 69px; top: 513px; font-size: 27px; color: var(--purple-text); }
  .about-text { left: 69px; top: 551px; width: 552px; font-size: 11px; line-height: 19px; color: var(--body); }
  .about-text p + p { margin-top: 9px; }

  .alt-title { left: 656px; top: 517px; font-size: 24px; color: var(--gold); }
  .alt-image { left: 657px; top: 549px; width: 272px; height: 107px;
    background: linear-gradient(135deg, #eef2f7 0%, #cfe0f0 50%, #4a86d0 100%); }
  .card-heading { font-size: 13px; color: #333; font-weight: 400; }
  .card-text { font-size: 10.5px; line-height: 16px; color: var(--body); }

  .divider { left: 90px; top: 766px; width: 830px; height: 30px;
    background: radial-gradient(ellipse at 50% 0%, rgba(0,0,0,.08) 0%, rgba(0,0,0,0) 70%); }
  .divider-notch { left: 485px; top: 764px; }

  .col-title { top: 838px; font-size: 21px; text-transform: uppercase; color: #222; }
  .col-title.gold { color: var(--gold); }
  .strategy-image { left: 63px; top: 870px; width: 272px; height: 94px;
    background: linear-gradient(90deg, #6b8fb2 0%, #cfdbe6 45%, #e9eef3 100%); }

  .check-list { left: 372px; top: 932px; list-style: none; }
  .check-list li { display: flex; align-items: center; gap: 7px; font-size: 11px; color: var(--purple-text); height: 23.5px; }

  .site-footer { left: 0; top: 1103px; width: 1003px; height: 97px; background: var(--purple); border-top: 1px solid #4c6aa0; }
  .footer-nav { left: 65px; top: 1127px; font-size: 12px; color: var(--white); }
  .footer-nav a { color: var(--white); text-decoration: none; }
  .footer-nav .sep { margin: 0 7px; }
  .copyright { left: 64px; top: 1153px; font-size: 11px; color: #d9d3e4; }
  .social { left: 851px; top: 1124px; display: flex; gap: 4px; }
  .social span { width: 24px; height: 24px; border-radius: 50%; background: var(--white); }
</style>
</head>
<body>

<header class="abs site-header"></header>
<svg class="abs brand-plate" width="287" height="102" viewBox="0 0 287 102" aria-hidden="true">
  <defs><linearGradient id="gold" x1="0" y1="0" x2="0" y2="1"><stop offset="0" stop-color="#9e9762"/><stop offset="1" stop-color="#6f6a3c"/></linearGradient></defs>
  <polygon points="0,0 287,0 243,102 0,102" fill="url(#gold)"/>
</svg>
<div class="abs brand-name">Velquist</div>
<nav class="abs main-nav">
  <a href="#">HOME</a><a href="#">PROFILE</a><a href="#">INVESTMENT PROCESS</a><a href="#">INVESTMENT SOLUTIONS</a><a href="#">NEWS</a><a href="#">CONTACT</a>
</nav>

<div class="abs hero" role="img" aria-label="Night view of a city avenue lined with lit skyscrapers"></div>
<h1 class="abs hero-title line-1">Growing Wealth</h1>
<div class="abs hero-title line-2">Preserving Capital</div>
<svg class="abs hero-arrow" style="left:52px" width="30" height="64" viewBox="0 0 30 64" aria-hidden="true"><polyline points="28,2 2,32 28,62" fill="none" stroke="rgba(255,255,255,.5)" stroke-width="2"/></svg>
<svg class="abs hero-arrow" style="left:922px" width="30" height="64" viewBox="0 0 30 64" aria-hidden="true"><polyline points="2,2 28,32 2,62" fill="none" stroke="rgba(255,255,255,.5)" stroke-width="2"/></svg>
<div class="abs hero-dots"><span class="active"></span><span></span><span></span><span></span></div>

<h2 class="abs section-title about-title">About Our Company</h2>
<div class="abs about-text">
  <p>Quisque dignissim congue leo.auris vel lacus vitae felis vestibulum volutpat. Etiam est nunc, venenatis in, tristique eu, imperdiet ac, nisl. Cum sociis natoque penatibus et magnis dis parturient montes, nascetur ridiculus mus. In iaculis facilisis massa. Etiam eu urna. Sed porta. Suspendisse quam leo, molestie sed, luctus quis, feugiat in, pede. Fusce tellus. Sed metus augue, convallis</p>
  <p>Etiam est nunc, venenatis in, tristique eu, imperdiet ac, nisl. Cum sociis natoque penatibus et magnis dis arturient montes, nascetur ridiculus mus. In iaculis facilisis massa. Etiam eu urna. Sed porta. Suspendisse quam leo, molestie sed, luctus quis, feugiat in, pede. Fusce tellus.</p>
</div>

<h2 class="abs section-title alt-title">Alternative Investments</h2>
<div class="abs alt-image" role="img" aria-label="Financial report with a rising bar chart"></div>
<h3 class="abs card-heading" style="left:657px;top:663px">Cum sociis natoque penatibus</h3>
<p class="abs card-text" style="left:658px;top:683px;width:270px">et magnis dis arturient montes, nascetur ridiculus mus. In iaculis facilisis massa. Etiam eu urna.</p>

<div class="abs divider"></div>
<svg class="abs divider-notch" width="30" height="16" viewBox="0 0 30 16" aria-hidden="true"><polygon points="0,0 30,0 15,15" fill="#fff"/></svg>

<h2 class="abs section-title col-title" style="left:63px">Investment Strategy</h2>
<div class="abs strategy-image" role="img" aria-label="Businessman in a suit drawing a rising growth line"></div>
<h3 class="abs card-heading" style="left:64px;top:971px;font-size:14px">Suspendisse vulputate aliquam</h3>
<p class="abs card-text" style="left:65px;top:995px;width:275px;line-height:17px">Nunc tempus felis vitae urna. Vivamus porttitor, g, purus nisi eleifend libero, a tempus libero lectus feugiat felis. Morbi diam mauris, viverra in, gravida eu, mattis in, ante. Morbi eget arcu. Morbi porta, libero</p>

<h2 class="abs section-title col-title" style="left:368px">Services Provide</h2>
<p class="abs card-text" style="left:370px;top:868px;width:245px;line-height:19px">Suspendisse vulputate aliquam dui. Nulla elementum dui ut augue. Aliquam vehicula mi at mauris. Maecenas placerat, nisl at consequat rhoncu</p>
<ul class="abs check-list">
  <li><svg width="13" height="11" viewBox="0 0 13 11" aria-hidden="true"><polyline points="1,6 5,10 12,1" fill="none" stroke="#3a2a64" stroke-width="2.4"/></svg>Etiam est nunc venenatis</li>
  <li><svg width="13" height="11" viewBox="0 0 13 11" aria-hidden="true"><polyline points="1,6 5,10 12,1" fill="none" stroke="#3a2a64" stroke-width="2.4"/></svg>Tristique eu imperdiet ac nisl</li>
  <li><svg width="13" height="11" viewBox="0 0 13 11" aria-hidden="true"><polyline points="1,6 5,10 12,1" fill="none" stroke="#3a2a64" stroke-width="2.4"/></svg>Cum sociis natoque</li>
  <li><svg width="13" height="11" viewBox="0 0 13 11" aria-hidden="true"><polyline points="1,6 5,10 12,1" fill="none" stroke="#3a2a64" stroke-width="2.4"/></svg>Penatibus et magnis</li>
  <li><svg width="13" height="11" viewBox="0 0 13 11" aria-hidden="true"><polyline points="1,6 5,10 12,1" fill="none" stroke="#3a2a64" stroke-width="2.4"/></svg>dis parturient montes</li>
</ul>

<h2 class="abs section-title col-title gold" style="left:656px">News &amp; Views</h2>
<h3 class="abs card-heading" style="left:658px;top:871px;font-weight:600;font-size:12px">Conec convallis pede venenatis</h3>
<p class="abs card-text" style="left:658px;top:892px;width:290px">Etiam est nunc, venenatis in, tristique eu, imperdiet nisl. Cum sociis natoque penatibus et magnis dis parturient montes,</p>
<h3 class="abs card-heading" style="left:658px;top:938px;font-weight:600;font-size:12px">Nulla sit amet diam</h3>
<p class="abs card-text" style="left:658px;top:960px;width:290px">Duis non nunc. Nulla rhoncus dictum metus. Curabitur tristique mi condimentum orci. Phasellus pellentesque aliquam enim</p>
<h3 class="abs card-heading" style="left:656px;top:1023px;font-weight:600;font-size:12px">Curabitur vel mi sit amet</h3>
<p class="abs card-text" style="left:656px;top:1044px;width:290px">Curabitur tristique mi condimentum orci Phasellus</p>

<footer class="abs site-footer"></footer>
<nav class="abs footer-nav">
  <a href="#">HOME</a><span class="sep">|</span><a href="#">PROFILE</a><span class="sep">|</span><a href="#">INVESTMENT PROCESS</a><span class="sep">|</span><a href="#">INVESTMENT SOLUTIONS</a><span class="sep">|</span><a href="#">NEWS</a><span class="sep">|</span><a href="#">CONTACT</a>
</nav>
<div class="abs copyright">© 2014 Company Name.&nbsp; All right reserved.&nbsp; Term of Use</div>
<div class="abs social" aria-label="Social links"><span></span><span></span><span></span></div>

</body>
</html>
```